Why Use Me?

Need to create several flyers to promote myself and various home mortgage loan products. I am a loan officer within a larger company so I'm looking for an attractive flyer frame that incorporates my company's colors & logo BUT it has my own custom look and feel. Once this frame is created, I'll have several ideas for body filler. I'm looking for a logo or moniker for myself, synonymous with my business.

```html
<!DOCTYPE html>
<html lang="en">
<head>
<meta charset="utf-8">
<title>Why Use Me? – Loan Officer Flyer</title>
<link rel="stylesheet" href="https://fonts.googleapis.com/css2?family=Libre+Baskerville:wght@400;700&family=Roboto+Condensed:wght@400&display=swap">
<style>
  :root {
    --page-bg: #e4e4e4;
    --navy: #1b2550;
    --cyan: #1aa7df;
    --cyan-bright: #1db3e8;
    --cyan-deep: #1681b8;
    --teal-dark: #1f4656;
    --teal-mid: #19849f;
    --white: #ffffff;
    --panel-light: #f2f2f2;
    --panel-grey: #d2d2d2;
  }
  * { margin: 0; padding: 0; box-sizing: border-box; }
  html, body {
    width: 1200px;
    height: 991px;
    overflow: hidden;
    background: var(--page-bg);
  }
  .flyer {
    position: absolute;
    left: 120px;
    top: 18px;
    width: 960px;
    height: 956px;
    overflow: hidden;
    background: radial-gradient(circle at 40% 42%, var(--panel-light) 0%, #e6e6e6 35%, var(--panel-grey) 100%);
    box-shadow: 0 3px 6px rgba(0,0,0,0.35);
  }
  .flyer-art {
    position: absolute;
    inset: 0;
    width: 960px;
    height: 956px;
  }
  .brand {
    position: absolute;
    left: 82px;
    top: 88px;
    display: flex;
    align-items: center;
    gap: 14px;
  }
  .brand-dot {
    width: 34px;
    height: 34px;
    border-radius: 50%;
    background: var(--cyan);
  }
  .brand-name {
    font-family: "Libre Baskerville", serif;
    font-weight: 400;
    font-size: 30px;
    letter-spacing: 1px;
    color: var(--navy);
  }
  .headline {
    position: absolute;
    left: 58px;
    top: 184px;
    font-family: "Libre Baskerville", serif;
    font-weight: 700;
    line-height: 1;
  }
  .headline-line {
    display: block;
    color: var(--navy);
    font-size: 88px;
    letter-spacing: 1px;
  }
  .headline-line + .headline-line { margin-top: 6px; }
  .headline-accent {
    display: block;
    color: var(--cyan);
    font-size: 140px;
    margin-top: -4px;
    letter-spacing: -2px;
  }
  .benefits {
    position: absolute;
    left: 40px;
    top: 570px;
    width: 360px;
    list-style: none;
    font-family: "Roboto Condensed", sans-serif;
    font-size: 19.5px;
    line-height: 27px;
    color: var(--white);
  }
  .benefits li {
    position: relative;
    padding-left: 26px;
  }
  .benefits li::before {
    content: "";
    position: absolute;
    left: 2px;
    top: 9px;
    border-left: 11px solid var(--white);
    border-top: 6px solid transparent;
    border-bottom: 6px solid transparent;
  }
  .web-link {
    position: absolute;
    left: 57px;
    top: 858px;
    width: 399px;
    height: 42px;
    border-radius: 5px;
    background: linear-gradient(90deg, var(--teal-dark) 0%, var(--teal-mid) 45%, var(--teal-mid) 55%, var(--teal-dark) 100%);
    box-shadow: 0 8px 8px -4px rgba(0,0,0,0.45);
    font-family: "Roboto Condensed", sans-serif;
    font-size: 28px;
    line-height: 42px;
    text-align: center;
    color: var(--white);
  }
</style>
</head>
<body>
  <main class="flyer">
    <svg class="flyer-art" viewBox="0 0 960 956" xmlns="http://www.w3.org/2000/svg">
      <defs>
        <linearGradient id="benefit-band" x1="0" y1="0" x2="1" y2="0">
          <stop offset="0" stop-color="#1a9fd8"/>
          <stop offset="0.5" stop-color="#1db3e8"/>
          <stop offset="1" stop-color="#1681b8"/>
        </linearGradient>
        <linearGradient id="accent-ring" x1="0" y1="0" x2="0" y2="1">
          <stop offset="0" stop-color="#1770a8"/>
          <stop offset="0.45" stop-color="#1db3e8"/>
          <stop offset="1" stop-color="#1a7fb3"/>
        </linearGradient>
        <linearGradient id="portrait-tones" x1="0" y1="0" x2="0" y2="1">
          <stop offset="0" stop-color="#eeeeee"/>
          <stop offset="0.55" stop-color="#d9c3b2"/>
          <stop offset="0.75" stop-color="#7f9fd6"/>
          <stop offset="1" stop-color="#1d2430"/>
        </linearGradient>
      </defs>
      <rect class="benefit-band" x="5" y="550" width="600" height="275" fill="url(#benefit-band)"/>
      <circle class="accent-ring" cx="983" cy="520" r="570" fill="url(#accent-ring)"/>
      <circle class="portrait-area" cx="983" cy="520" r="526" fill="url(#portrait-tones)"
              role="img" aria-label="Portrait photo of the loan officer in a dark suit, blue shirt and striped tie"/>
    </svg>

    <div class="brand">
      <span class="brand-dot"></span>
      <span class="brand-name">NORTHVALE LENDING</span>
    </div>

    <h1 class="headline">
      <span class="headline-line">WHY</span>
      <span class="headline-line">USE</span>
      <span class="headline-accent">ME?</span>
    </h1>

    <ul class="benefits">
      <li>I’m 17 years at the same exact mortgage company</li>
      <li>Very knowledgeable</li>
      <li>Above and beyond service and availability</li>
      <li>Conversion of tough loans</li>
      <li>“Build a Buyer” program</li>
      <li>Excellent follow-up</li>
      <li>I work with a seasoned lending team</li>
    </ul>

    <div class="web-link">www.northvalelending.com</div>
  </main>
</body>
</html>
```